Re-design an HTML Website

Website must be responsive/fluid and designed with mobile-first priority. I want to be able to make changes with a HTML editor

We offer EMF Protection devices that neutralize EMF radiations emitted from electronics. We have devices for people and cell phones.
.

Redesign our Website (www.brightpebs.us) to look more modern, but I need to keep it in an HTML format. I plan on keeping the same shopping cart service (CartHarbor.com), as it has some features we need, but it is BUTTON intensive.

Requirements requested (samples submitted):
Headers and Footers
Menu setup as submitted
Creative Landing Page
Categories Page (must be stacked products)
Products Page (must be stacked products)
Individual Product Page
Generic 1-Column Page
Generic 2-Column Page
Generic 3-Column Page
Updates

What we sell are devices to neutralize the electromagnetic radiation (EMF) emitted from cell phones and electronics. Anything thing you can do to bring this website (www.BrightPEBs.us) into the 21st Century will be appreciated. It is a secondary website for our Affiliate Accounts - our primary site is at Vendora www.TopWaveGoods.com

Be creative -- make us look and feel great!

Thanks, Dorian

Providing both a Mobile & Desktop screen shot would be helpful.

Also, do not use the products from vitalorbs.com - it is a slightly different product.
www.TopWaveGoods.com or www.BrightPEBs.us are our product configurations.

Industry/Entity Type

Technologoy

Coding

Coded - Design and coding required

Number of Pages Required

5+ page

Requirements
Must have
• Zip file and desciptions included
Nice to have
• Menu / footer /header / Landing page / Product Page / Category Page

```html
<!DOCTYPE html>
<html lang="en">
<head>
<meta charset="utf-8">
<title>Bright PEB – EMF Protection</title>
<link href="https://fonts.googleapis.com/css2?family=Poppins:ital,wght@0,400;0,500;0,600;0,700;0,800;1,400;1,600&family=Roboto:wght@400;500;700&family=Tinos:wght@700&display=swap" rel="stylesheet">
<style>
:root{
  --orange:#f5a800;
  --orange-dark:#e39500;
  --ink:#111111;
  --text:#333333;
  --muted:#6d6d6d;
  --paper:#ffffff;
  --soft:#f2f2f2;
  --stage:#5e5e5e;
  --sky:#1eaaf1;
  --price:#d9232d;
}
*{box-sizing:border-box;margin:0;padding:0}
html,body{width:1200px;height:3122px;overflow:hidden}
body{background:var(--stage);font-family:"Roboto",sans-serif;color:var(--text);position:relative}
.abs{position:absolute}
.heading{font-family:"Poppins",sans-serif;font-weight:700;color:var(--ink)}
.accent{color:var(--orange)}
.btn{position:absolute;display:flex;align-items:center;justify-content:center;gap:5px;background:var(--orange);color:#fff;font-family:"Poppins",sans-serif;font-weight:600;border-radius:40px;letter-spacing:.2px}
.btn::after{content:"";width:7px;height:7px;border-radius:50%;background:#fff}
.btn.plain::after{display:none}
.btn.outline{background:#fff;border:1.5px solid var(--orange);color:var(--ink)}
.btn.outline::after{background:var(--ink)}
.photo{position:absolute;overflow:hidden}
.tick{display:inline-flex;align-items:center;gap:5px}
p.tick{display:flex}
.tick::before{content:"";width:8px;height:8px;border-radius:50%;background:var(--ink);flex:none}
.circle-arrow{position:absolute;border-radius:50%;display:flex;align-items:center;justify-content:center;font-family:"Poppins",sans-serif;font-weight:700}

/* desktop frame */
.desktop{position:absolute;left:44px;top:44px;width:855px;height:3032px;background:var(--paper);overflow:hidden}
.topbar{position:absolute;left:0;top:0;width:855px;height:25px;background:var(--orange);font-family:"Poppins",sans-serif;font-size:11px;color:var(--ink);font-weight:500}
.topbar .sep{position:absolute;top:0;width:1px;height:25px;background:rgba(0,0,0,.15)}
.nav{position:absolute;left:0;top:25px;width:855px;height:57px;background:#f6f6f6}
.wordmark{position:absolute;font-family:"Poppins",sans-serif;font-weight:600;color:var(--ink);letter-spacing:.3px;white-space:nowrap}
.menu{position:absolute;left:206px;top:22px;display:flex;gap:15px;font-family:"Poppins",sans-serif;font-size:10px;font-weight:500;color:var(--ink)}
.menu span.drop::after{content:" ▾";font-size:8px}
.hero{position:absolute;left:0;top:82px;width:855px;height:470px;background:linear-gradient(100deg,#f6efe6 0%,#efe2d2 30%,#c9a98a 55%,#b9875a 72%,#e59b3e 88%,#8a5a34 100%)}
.hero-title{position:absolute;left:80px;font-family:"Poppins",sans-serif;font-weight:700;font-size:32px;line-height:40px;color:var(--ink)}
.card{position:absolute;overflow:hidden;background:linear-gradient(90deg,#fde9d5 0%,#fbe6d3 45%,#f6dcc3 100%)}
.card .body{position:absolute;left:20px;top:18px;font-family:"Poppins",sans-serif;color:var(--ink)}
.card h3{font-size:14px;font-weight:600;line-height:24px}
.card p{font-size:11px;line-height:20px}
.price{font-family:"Poppins",sans-serif;font-weight:600;color:var(--price)}
.select{position:absolute;background:#fff;border-radius:14px;box-shadow:0 1px 4px rgba(0,0,0,.08);font-family:"Roboto",sans-serif;font-size:12px;color:var(--ink);display:flex;align-items:center;justify-content:space-between;padding:0 12px 0 16px}
.select::after{content:"";border-left:4px solid transparent;border-right:4px solid transparent;border-top:5px solid var(--ink)}
.tile{position:absolute;overflow:hidden;color:#fff;text-align:center;font-family:"Poppins",sans-serif}
.tile b{position:absolute;left:0;width:100%;font-size:12px;font-weight:600}
.tile em{position:absolute;left:0;width:100%;font-size:12px}
.bundle{position:absolute;background:var(--orange);border-radius:90px}
.footer{position:absolute;background:#000;color:#fff}
.footer .col-title{font-family:"Poppins",sans-serif;font-size:10px;font-weight:600}
.footer .link{font-size:9px}
.pay{display:inline-block;width:20px;height:12px;border-radius:2px;background:#fff;margin-right:6px;border:1px solid #ccc}

/* mobile frame */
.mobile{position:absolute;left:927px;top:44px;width:230px;height:1980px;background:var(--paper);overflow:hidden}
.m-card{position:absolute;background:#fff;overflow:hidden;font-family:"Poppins",sans-serif;color:var(--ink)}
.m-card .t{position:absolute;left:5px;font-size:5.5px;line-height:8px}
</style>
</head>
<body>

<!-- ============ DESKTOP ============ -->
<main class="desktop">
  <div class="topbar">
    <span class="abs" style="left:80px;top:5px">Follow Us</span>
    <span class="sep" style="left:147px"></span>
    <span class="abs" style="left:158px;top:8px;width:8px;height:8px;border-radius:50%;background:var(--ink)"></span>
    <span class="sep" style="left:180px"></span>
    <span class="abs" style="left:192px;top:8px;width:8px;height:8px;border-radius:2px;background:var(--ink)"></span>
    <span class="sep" style="left:214px"></span>
    <span class="abs" style="left:0;width:855px;text-align:center;top:5px;font-weight:600">Free Shipping Over $299</span>
    <svg class="abs" style="left:722px;top:4px" width="17" height="17" viewBox="0 0 17 17"><circle cx="8.5" cy="8.5" r="8.5" fill="#fff"/><path d="M6 5l1.5 1.5-1 1a5 5 0 0 0 2.5 2.5l1-1L11.5 10.5 10.5 12C7 12 5 9 5 6z" fill="#111"/></svg>
    <svg class="abs" style="left:752px;top:4px" width="17" height="17" viewBox="0 0 17 17"><circle cx="8.5" cy="8.5" r="8.5" fill="#fff"/><rect x="5" y="6" width="7" height="5" fill="#111"/><path d="M5 6l3.5 3L12 6" stroke="#fff" fill="none" stroke-width=".8"/></svg>
  </div>

  <header class="nav">
    <div class="wordmark" style="left:52px;top:15px;font-size:18px">Bright Peb</div>
    <nav class="menu">
      <span>Home</span><span class="drop">EMF Protection Devices</span><span class="drop">Savings Options</span><span class="drop">Why these Products</span><span class="drop">Newsletter</span><span class="drop">Other Products</span><span class="drop">About Us</span>
    </nav>
  </header>

  <section class="hero" role="img" aria-label="Smiling woman in an orange sweater working on a laptop at a wooden desk">
    <div class="hero-title" style="top:105px"><span class="accent">Best</span> EMF Products</div>
    <div class="hero-title" style="top:151px"><span class="accent">Practical</span> EMF</div>
    <div class="hero-title" style="top:189px">Solutions</div>
    <div class="btn" style="left:83px;top:251px;width:110px;height:30px;font-size:10px">SHOP NOW</div>
    <svg class="abs" style="left:0;top:350px" width="855" height="120" viewBox="0 0 855 120" preserveAspectRatio="none">
      <path d="M0 50 C120 110 230 100 380 75 C540 45 700 25 855 20 L855 120 L0 120 Z" fill="var(--orange)"/>
      <path d="M0 62 C120 112 240 110 390 88 C550 64 710 46 855 40 L855 120 L0 120 Z" fill="#fff"/>
    </svg>
  </section>

  <!-- categories -->
  <article class="card" style="left:93px;top:630px;width:317px;height:183px">
    <div class="photo" role="img" aria-label="Two colleagues smiling at a laptop in an office" style="left:140px;top:0;width:177px;height:183px;background:linear-gradient(90deg,rgba(251,230,211,0) 0%,#d9c3ad 35%,#b8a690 70%,#9a8c7f 100%)"></div>
    <div class="body">
      <h3>Bright PEBs</h3>
      <h3>For All Electronics</h3>
      <p style="margin-top:2px">Use Bright PEBs on</p>
      <p class="tick">Smartphones</p>
      <p class="tick">Computers</p>
    </div>
    <div class="btn" style="left:20px;top:138px;width:110px;height:28px;font-size:10px">BUY NOW</div>
  </article>

  <article class="card" style="left:424px;top:630px;width:333px;height:183px">
    <div class="photo" role="img" aria-label="Person in a black sweater wearing a protective wrist band" style="left:150px;top:0;width:183px;height:183px;background:linear-gradient(90deg,rgba(251,230,211,0) 0%,#6b5b4e 30%,#1c1c1c 60%,#e8d8c6 100%)"></div>
    <div class="body" style="top:26px">
      <h3>Starter Packages</h3>
      <h3>For You</h3>
      <p style="margin-top:6px">1 Wearable + 1 Bright PEB</p>
      <p style="margin-top:6px"><span class="tick">Pendant</span><span class="tick" style="margin-left:36px">Clip</span></p>
    </div>
    <div class="price abs" style="left:20px;top:135px;font-size:18px">$69.95</div>
    <div class="btn" style="left:88px;top:132px;width:110px;height:28px;font-size:10px">BUY NOW</div>
  </article>

  <article class="card" style="left:93px;top:828px;width:664px;height:183px">
    <div class="photo" role="img" aria-label="Woman hugging a long-haired cat" style="left:380px;top:0;width:284px;height:183px;background:linear-gradient(90deg,rgba(251,230,211,0) 0%,#c9a183 35%,#7a5539 65%,#3a2a22 100%)"></div>
    <div class="abs heading" style="left:20px;top:20px;font-size:24px;font-weight:600">Other EMF Products <span style="font-size:17px;font-weight:500;margin-left:8px">For the Home</span></div>
    <div class="abs" style="left:26px;top:70px;font-family:Poppins,sans-serif;font-size:10px;color:var(--ink)">
      <div><span class="tick">Aqua PEB</span><span class="tick" style="margin-left:50px">Pet PEB</span><span class="tick" style="margin-left:42px">Space PRISM</span></div>
      <p class="tick" style="margin-top:15px">Grounding Mats &amp; Sheets</p>
    </div>
    <div class="price abs" style="left:24px;top:132px;font-size:18px">$69.95</div>
    <div class="btn" style="left:100px;top:128px;width:112px;height:29px;font-size:10px">BUY NOW</div>
  </article>

  <!-- featured product -->
  <section class="abs" style="left:0;top:1079px;width:855px;height:483px;background:var(--soft)">
    <h2 class="heading abs" style="left:0;top:48px;width:855px;text-align:center;font-size:31px"><span class="accent">Best</span> EMF Products</h2>
    <div class="circle-arrow" style="left:26px;top:266px;width:26px;height:26px;background:var(--orange);color:#111;font-size:12px">‹</div>
    <div class="abs" style="left:798px;top:270px;font-size:12px;color:#111">›</div>
    <div class="abs" role="img" aria-label="Silver laptop product shot" style="left:86px;top:129px;width:264px;height:289px;border-radius:28px;background:radial-gradient(circle at 50% 40%,#9fa3a8 0%,#6b6f74 22%,var(--sky) 23%,var(--sky) 100%)">
      <div class="btn plain" style="left:69px;top:250px;width:112px;height:38px;font-size:20px;border-radius:10px;color:#111">$ 199.95</div>
    </div>
    <h3 class="heading abs" style="left:397px;top:141px;font-size:16px;font-weight:600">Bright PEBs for All Electronics</h3>
    <p class="abs" style="left:397px;top:176px;width:380px;font-size:10.5px;line-height:17px;color:var(--muted)">Bright PEBs can be applied to any electronic device to change the EMF energies to be more human-compatible.</p>
    <div class="select" style="left:395px;top:234px;width:121px;height:26px">Colour</div>
    <div class="select" style="left:547px;top:234px;width:142px;height:26px">package</div>
    <div class="btn plain" style="left:698px;top:234px;width:74px;height:26px;font-size:10px">BUY</div>
    <h4 class="heading abs" style="left:397px;top:287px;font-size:12px;font-weight:600">Product Details</h4>
    <p class="abs" style="left:397px;top:313px;font-size:10.5px;line-height:16.5px;color:var(--muted)">Smart / cell phones / handsets<br>Wi-Fi modems, routers, &amp; boosters<br>Computers / Laptops<br>Utility smart meters (electric / gas / water)</p>
    <div class="abs" role="img" aria-label="Man using a tablet" style="left:607px;top:293px;width:76px;height:65px;background:linear-gradient(135deg,#c9ccd0,#54606c);border:4px solid #fff;box-shadow:0 1px 4px rgba(0,0,0,.1)"></div>
    <div class="abs" role="img" aria-label="Person working at a laptop" style="left:695px;top:293px;width:80px;height:65px;background:linear-gradient(135deg,#ede6df,#b08a6e);border:4px solid #fff;box-shadow:0 1px 4px rgba(0,0,0,.1)"></div>
    <div class="abs heading" style="left:397px;top:390px;font-size:10px;font-weight:600">VIEW MORE <span style="display:inline-block;width:8px;height:8px;border-radius:50%;background:#111;vertical-align:middle"></span></div>
  </section>

  <!-- explore -->
  <h2 class="heading abs" style="left:0;top:1614px;width:855px;text-align:center;font-size:31px"><span class="accent">Explore</span> The Range</h2>
  <div class="circle-arrow" style="left:26px;top:1772px;width:26px;height:26px;background:var(--orange);color:#111;font-size:12px">‹</div>
  <div class="circle-arrow" style="left:789px;top:1772px;width:26px;height:26px;background:#fff;box-shadow:0 1px 4px rgba(0,0,0,.15);color:#111;font-size:12px">›</div>

  <div class="tile" role="img" aria-label="Woman meditating on a beach at sunset" style="left:79px;top:1681px;width:214px;height:213px;background:linear-gradient(180deg,#8c8582,#4f4540 60%,#2e2623)">
    <b style="top:116px">BIOPEB</b><em style="top:140px">7 Products</em>
    <div class="btn plain" style="left:69px;top:170px;width:76px;height:24px;font-size:9.5px">SHOP NOW</div>
  </div>
  <div class="tile" role="img" aria-label="Bare feet resting on a blue acupressure mat" style="left:321px;top:1681px;width:214px;height:213px;background:linear-gradient(160deg,#2d2f42,#3a3f73 55%,#1f2030)">
    <b style="top:116px">SPACEPEB</b><em style="top:140px">3 Products</em>
    <div class="btn plain" style="left:69px;top:170px;width:76px;height:24px;font-size:9.5px">SHOP NOW</div>
  </div>
  <div class="tile" role="img" aria-label="Hand holding a smartphone above a keyboard" style="left:562px;top:1681px;width:215px;height:213px;background:linear-gradient(160deg,#45474c,#25272c 55%,#4b4c50)">
    <svg class="abs" style="left:85px;top:72px" width="44" height="30" viewBox="0 0 44 30"><path d="M4 12a26 26 0 0 1 36 0M10 18a17 17 0 0 1 24 0M16 24a8 8 0 0 1 12 0" stroke="#fff" stroke-width="3" fill="none" opacity=".8"/></svg>
    <b style="top:116px">FOR DEVICES</b><em style="top:140px">4 Products</em>
    <div class="btn plain" style="left:69px;top:170px;width:76px;height:24px;font-size:9.5px">SHOP NOW</div>
  </div>
  <div class="btn outline" style="left:372px;top:1916px;width:112px;height:32px;font-size:10px">VIEW MORE</div>

  <!-- bundle banner -->
  <section class="bundle" style="left:0;top:2014px;width:855px;height:175px">
    <div class="abs" style="left:34px;top:80px;font-size:12px;color:#111">‹</div>
    <div class="circle-arrow" style="left:790px;top:76px;width:24px;height:24px;background:#fff;color:#111;font-size:11px">›</div>
    <h2 class="heading abs" style="right:81px;top:35px;font-size:21px">BUNDLED PACKAGES</h2>
    <p class="abs" style="right:81px;top:81px;font-family:Poppins,sans-serif;font-style:italic;font-weight:600;font-size:10px;color:#111">It is important to cover more than just your smart phone!</p>
    <p class="abs" style="right:81px;top:106px;text-align:right;font-family:Poppins,sans-serif;font-style:italic;font-size:12.5px;line-height:21px;color:#111">Cover as many devices as you can afford:<br>Wi-Fi routers, computers, laptops, tables, etc</p>
  </section>
  <div class="photo" role="img" aria-label="Woman holding a laptop beside a large gold twenty percent off graphic" style="left:59px;top:1956px;width:323px;height:233px;background:linear-gradient(90deg,rgba(200,200,205,.95) 0%,#9a9aa2 35%,#e6b419 55%,#c99200 80%,rgba(245,168,0,0) 100%);border-radius:40px 0 0 0"></div>

  <!-- consultation -->
  <h2 class="heading abs" style="left:80px;top:2250px;font-size:31px"><span class="accent">Educational</span> Health Consultation</h2>
  <h3 class="heading abs" style="left:81px;top:2304px;font-size:16px;font-weight:600">with Helena Marsh, CLS, NCMP, Ph.D.</h3>
  <div class="abs" style="left:79px;top:2354px;width:360px;font-family:Poppins,sans-serif;font-size:10.5px;line-height:17px;color:var(--text)">
    <p>Understanding what you are going through and how to get help can be a difficult and tedious process.</p>
    <p style="margin-top:16px">Dr. Marsh's 25 years of experience allows her to quickly assess what works and what does not.</p>
    <p style="margin-top:16px">Her goal is to get you on the right track so that you can obtain the health care that is best for you and your family.</p>
    <p style="margin-top:14px;font-weight:600;font-size:12px;color:#111">Electromagnetic Sensitivity Consultations</p>
  </div>
  <div class="btn" style="left:81px;top:2546px;width:141px;height:30px;font-size:10px">CONSULTATION</div>
  <svg class="abs" style="left:470px;top:2310px" width="340" height="320" viewBox="0 0 340 320">
    <path d="M170 8 A150 150 0 0 1 250 290" stroke="var(--orange)" stroke-width="10" fill="none"/>
    <circle cx="160" cy="160" r="147" fill="#fff" stroke="#eee"/>
  </svg>
  <div class="abs" role="img" aria-label="Portrait of the consultant in a teal jacket" style="left:560px;top:2346px;width:130px;height:185px;border-radius:60px 60px 0 0;background:linear-gradient(180deg,#d9cfc8 0%,#7d5b48 30%,#1f6f74 55%,#1a5f64 100%)"></div>
  <p class="abs" style="left:539px;top:2543px;width:190px;text-align:center;font-family:Tinos,serif;font-weight:700;font-size:11px;color:#111">Helena Marsh,&nbsp; CLS, NCMP, PhD</p>

  <!-- footer -->
  <svg class="abs" style="left:0;top:2590px" width="855" height="90" viewBox="0 0 855 90" preserveAspectRatio="none">
    <path d="M0 62 C250 60 560 50 855 16" stroke="var(--orange)" stroke-width="6" fill="none"/>
    <path d="M0 70 C250 68 560 58 855 24 L855 90 L0 90 Z" fill="#000"/>
  </svg>
  <footer class="footer" style="left:0;top:2678px;width:855px;height:354px">
    <svg class="abs" style="left:118px;top:30px" width="34" height="22" viewBox="0 0 34 22"><path d="M2 3h18v13H2zM20 8h7l5 5v3H20z" stroke="#fff" fill="none" stroke-width="1.4"/><circle cx="8" cy="18" r="2.5" fill="#000" stroke="#fff" stroke-width="1.4"/><circle cx="26" cy="18" r="2.5" fill="#000" stroke="#fff" stroke-width="1.4"/></svg>
    <p class="abs" style="left:168px;top:20px;font-family:Poppins,sans-serif;font-size:10px;font-weight:500">Free shipping</p>
    <p class="abs accent" style="left:166px;top:38px;font-family:Poppins,sans-serif;font-size:15px;font-weight:600">over $299</p>
    <svg class="abs" style="left:358px;top:28px" width="28" height="28" viewBox="0 0 28 28"><circle cx="14" cy="14" r="11" stroke="#fff" fill="none" stroke-width="1.4"/><circle cx="14" cy="14" r="7" stroke="#fff" fill="none" stroke-width="1.2"/><path d="M10 14l3 3 5-6" stroke="#fff" fill="none" stroke-width="1.4"/></svg>
    <p class="abs" style="left:399px;top:20px;font-family:Poppins,sans-serif;font-size:10px;font-weight:500">Returns</p>
    <p class="abs accent" style="left:397px;top:38px;font-family:Poppins,sans-serif;font-size:15px;font-weight:600">180-Day</p>
    <svg class="abs" style="left:548px;top:30px" width="26" height="22" viewBox="0 0 26 22"><path d="M2 4h22v14H2z M2 4l11 8 11-8" stroke="#fff" fill="none" stroke-width="1.4"/></svg>
    <p class="abs" style="left:596px;top:20px;font-family:Poppins,sans-serif;font-size:10px;font-weight:500">Contact</p>
    <p class="abs" style="left:596px;top:45px;font-family:Poppins,sans-serif;font-size:9px;line-height:17px">555 014-2268 Fairview, CA USA<br>info@TopWaveGoods.com<br>Modern Wellness Advisors LLC</p>
    <div class="abs" style="left:79px;top:125px;width:697px;border-top:1px dashed #555"></div>
    <div class="wordmark" style="left:80px;top:144px;font-size:17px;color:#fff">Bright Peb</div>
    <p class="abs col-title" style="left:80px;top:192px">Quick Links</p>
    <p class="abs link" style="left:80px;top:215px;line-height:19.5px">Search<br>Contact Information<br>Privacy Policy</p>
    <p class="abs col-title" style="left:275px;top:192px">Other Links</p>
    <p class="abs link" style="left:275px;top:215px;line-height:19.5px">Refund Policy<br>Shipping Policy<br>Terms of Service</p>
    <p class="abs col-title" style="left:433px;top:192px">Subscribe to our newsletter</p>
    <div class="abs" style="left:433px;top:215px;width:130px;height:22px;border-radius:12px;background:#fff;font-size:9px;color:#777;padding:5px 12px">Enter Email</div>
    <svg class="abs" style="left:541px;top:215px" width="22" height="22" viewBox="0 0 22 22"><circle cx="11" cy="11" r="11" fill="var(--orange)"/><path d="M7 6l9 5-9 5 2-5z" fill="#111"/></svg>
    <div class="abs" style="left:436px;top:269px"><span class="pay"></span><span class="pay"></span><span class="pay"></span><span class="pay"></span><span class="pay"></span><span class="pay"></span><span class="pay"></span></div>
    <p class="abs col-title" style="left:730px;top:192px">Follow Us</p>
    <span class="abs" style="left:730px;top:216px;width:7px;height:7px;border-radius:50%;background:#fff"></span>
    <span class="abs" style="left:755px;top:216px;width:7px;height:7px;border-radius:2px;background:#fff"></span>
    <p class="abs" style="left:0;width:855px;text-align:center;top:318px;font-family:Poppins,sans-serif;font-size:9px">Copyright@2024 - All Rights Reserved By Bright PEB</p>
  </footer>
</main>

<!-- ============ MOBILE ============ -->
<main class="mobile">
  <div class="wordmark" style="left:17px;top:3px;font-size:8px">Bright Peb</div>
  <svg class="abs" style="left:205px;top:5px" width="9" height="7" viewBox="0 0 9 7"><path d="M0 .5h9M0 3.5h9M0 6.5h9" stroke="#111"/></svg>
  <section class="abs" role="img" aria-label="Smiling woman in an orange sweater working on a laptop" style="left:0;top:17px;width:230px;height:135px;background:linear-gradient(100deg,#f6efe6 0%,#efe2d2 35%,#c9a98a 60%,#e59b3e 85%,#8a5a34 100%)">
    <div class="heading abs" style="left:17px;top:19px;font-size:10px;line-height:14px"><span class="accent">Best</span> EMF Products</div>
    <div class="heading abs" style="left:17px;top:34px;font-size:8px;line-height:13px"><span class="accent">Practical</span> EMF<br>Solutions</div>
    <div class="btn" style="left:17px;top:78px;width:50px;height:14px;font-size:5px">SHOP NOW</div>
    <svg class="abs" style="left:0;top:100px" width="230" height="35" viewBox="0 0 230 35" preserveAspectRatio="none"><path d="M0 15 C60 35 140 30 230 8 L230 35 L0 35Z" fill="var(--orange)"/><path d="M0 19 C60 37 140 34 230 14 L230 35 L0 35Z" fill="#fff"/></svg>
  </section>

  <section class="abs" style="left:0;top:152px;width:230px;height:190px;background:var(--soft)">
    <div class="m-card" role="img" aria-label="Woman hugging a cat" style="left:5px;top:16px;width:108px;height:76px;background:linear-gradient(135deg,#e7d6c6,#8a6a50 60%,#3a2a22)"></div>
    <div class="m-card" style="left:117px;top:16px;width:108px;height:66px;background:linear-gradient(90deg,#fde9d5 55%,#2a2a2a)">
      <p class="t" style="top:4px;font-weight:600">Starter Packages<br>For You</p>
      <p class="t" style="top:24px">1 Wearable + 1 Bright PEB<br>● Pendant &nbsp;&nbsp; ● Clip</p>
      <p class="t price" style="top:46px;font-size:6px">$69.95</p>
      <div class="btn" style="left:36px;top:46px;width:36px;height:10px;font-size:4.5px">BUY NOW</div>
    </div>
    <div class="m-card" style="left:5px;top:92px;width:108px;height:78px;background:linear-gradient(90deg,#fde9d5,#fbe6d3)">
      <p class="t" style="top:6px;font-weight:600">Other EMF Products<br>For the Home</p>
      <p class="t" style="top:26px;font-size:4.5px;line-height:8px">● Aqua PEB &nbsp; ● Pet PEB<br>● Grounding Mats &amp; Sheets<br>● Space PRISM &nbsp;&nbsp;&nbsp; <span class="price">$69.95</span></p>
      <div class="btn" style="left:5px;top:62px;width:36px;height:10px;font-size:4.5px">BUY NOW</div>
    </div>
    <div class="m-card" style="left:117px;top:86px;width:108px;height:84px;background:linear-gradient(90deg,#fde9d5 50%,#a69686)">
      <p class="t" style="top:6px;font-weight:600">Bright PEBs<br>For All Electronics</p>
      <p class="t" style="top:23px;font-size:4.8px">Use Bright PEBs on<br>● Smartphones<br>● Computers</p>
      <div class="btn" style="left:13px;top:66px;width:36px;height:10px;font-size:4.5px">BUY NOW</div>
    </div>
  </section>

  <section class="abs" style="left:0;top:342px;width:230px;height:414px;background:var(--soft)">
    <p class="heading abs" style="left:19px;top:20px;font-size:10px;font-weight:600"><span class="accent">Best</span> EMF Products</p>
    <span class="abs" style="left:180px;top:23px;width:11px;height:11px;border-radius:50%;background:var(--orange)"></span>
    <span class="abs" style="left:200px;top:23px;width:11px;height:11px;border-radius:50%;background:#fff"></span>
    <p class="abs" style="left:21px;top:40px;font-size:5px;font-weight:700;color:#111">Bright PEBs for All Electronics</p>
    <p class="abs" style="left:21px;top:56px;width:165px;font-size:4.5px;line-height:7px;color:var(--muted)">Bright PEBs can be applied to any electronic device to change the EMF energies to be more human-compatible.</p>
    <div class="select" style="left:10px;top:89px;width:75px;height:12px;font-size:5px;padding:0 5px">Colour</div>
    <div class="select" style="left:103px;top:89px;width:75px;height:12px;font-size:5px;padding:0 5px">package</div>
    <div class="btn plain" style="left:190px;top:89px;width:34px;height:12px;font-size:5px">BUY</div>
    <div class="abs" role="img" aria-label="Silver laptop product shot" style="left:30px;top:127px;width:172px;height:185px;border-radius:20px;background:radial-gradient(circle at 50% 40%,#9fa3a8 0%,#6b6f74 22%,var(--sky) 23%);box-shadow:0 3px 8px rgba(0,0,0,.15)">
      <div class="btn plain" style="left:58px;top:157px;width:45px;height:14px;font-size:7px;color:#111;border-radius:5px">$ 199.95</div>
    </div>
    <p class="abs" style="left:22px;top:346px;font-size:6.5px;font-weight:700;color:#111">Product Details</p>
    <p class="abs" style="left:22px;top:360px;font-size:4.2px;line-height:6px;color:var(--muted)">Smart / cell phones / handsets<br>Wi-Fi modems, routers, &amp; boosters<br>Computers / Laptops<br>Utility smart meters (electric / gas / water)</p>
    <div class="abs" role="img" aria-label="Man using a tablet" style="left:125px;top:350px;width:50px;height:43px;border:2px solid #fff;background:linear-gradient(135deg,#c9ccd0,#54606c)"></div>
    <div class="abs" role="img" aria-label="Person working at a laptop" style="left:185px;top:350px;width:45px;height:43px;border:2px solid #fff;background:linear-gradient(135deg,#ede6df,#b08a6e)"></div>
    <p class="abs" style="left:22px;top:402px;font-size:5px;font-weight:700;color:#111">VIEW MORE ●</p>
  </section>

  <span class="abs" style="left:17px;top:801px;width:11px;height:11px;border-radius:50%;background:var(--orange)"></span>
  <span class="abs" style="left:202px;top:801px;width:11px;height:11px;border-radius:50%;background:#f1f1f1"></span>
  <p class="heading abs" style="left:0;width:230px;text-align:center;top:800px;font-size:10px;font-weight:600"><span class="accent">Explore</span> The Range</p>
  <div class="tile" role="img" aria-label="Bare feet on a blue acupressure mat" style="left:12px;top:825px;width:98px;height:98px;background:linear-gradient(160deg,#2d2f42,#3a3f73 55%,#1f2030)">
    <b style="top:56px;font-size:6px">SPACEPEB</b><em style="top:66px;font-size:5px">3 Products</em>
    <div class="btn" style="left:22px;top:84px;width:50px;height:10px;font-size:4.5px">BUY NOW</div>
  </div>
  <div class="tile" role="img" aria-label="Hand holding a phone above a keyboard" style="left:119px;top:825px;width:99px;height:98px;background:linear-gradient(160deg,#45474c,#25272c 55%,#4b4c50)">
    <b style="top:56px;font-size:6px">FOR DEVICES</b><em style="top:66px;font-size:5px">4 Products</em>
    <div class="btn" style="left:22px;top:84px;width:50px;height:10px;font-size:4.5px">BUY NOW</div>
  </div>
  <div class="btn outline" style="left:86px;top:945px;width:58px;height:16px;font-size:5px">VIEW MORE</div>

  <section class="abs" style="left:0;top:1018px;width:230px;height:215px;background:var(--orange)">
    <p class="heading abs" style="left:0;width:230px;text-align:center;top:124px;font-size:8px">BUNDLED PACKAGES</p>
    <p class="abs" style="left:0;width:230px;text-align:center;top:148px;font-family:Poppins,sans-serif;font-style:italic;font-weight:600;font-size:4.8px;line-height:8px;color:#111">It is important to cover more than just your smart phone!</p>
    <p class="abs" style="left:0;width:230px;text-align:center;top:162px;font-family:Poppins,sans-serif;font-style:italic;font-size:4.8px;line-height:8px;color:#111">Cover as many devices as you can afford:<br>Wi-Fi routers, computers, laptops, tables, etc</p>
    <span class="abs" style="left:100px;top:190px;width:11px;height:11px;border-radius:50%;background:var(--orange-dark)"></span>
    <span class="abs" style="left:119px;top:190px;width:11px;height:11px;border-radius:50%;background:#fff"></span>
  </section>
  <div class="photo" role="img" aria-label="Woman holding a laptop beside a gold twenty percent off graphic" style="left:0;top:975px;width:230px;height:152px;background:linear-gradient(90deg,rgba(190,190,196,.95) 0%,#9a9aa2 25%,#e6b419 50%,#c99200 80%,var(--orange) 100%)"></div>

  <p class="heading abs" style="left:17px;top:1256px;font-size:9.5px;font-weight:600"><span class="accent">Educational</span> Health Consultation</p>
  <p class="abs" style="left:19px;top:1275px;font-size:5px;font-weight:700;color:#111">with Helena Marsh, CLS, NCMP, Ph.D.</p>
  <div class="abs" style="left:17px;top:1293px;width:196px;font-size:4.2px;line-height:6px;color:var(--text)">
    <p>Understanding what you are going through and how to get help can be a difficult and tedious process.</p>
    <p style="margin-top:5px">Dr. Marsh's 25 years of experience allows her to quickly assess what works and what does not.</p>
    <p style="margin-top:5px">Her goal is to get you on the right track so that you can obtain the health care that is best for you and your family.</p>
    <p style="margin-top:5px;font-weight:700;color:#111;font-size:4.8px">Electromagnetic Sensitivity Consultations</p>
  </div>
  <svg class="abs" style="left:18px;top:1372px" width="196" height="190" viewBox="0 0 196 190"><path d="M100 4 A90 90 0 0 1 150 170" stroke="var(--orange)" stroke-width="5" fill="none"/><circle cx="94" cy="93" r="88" fill="#fff" stroke="#eee"/></svg>
  <div class="abs" role="img" aria-label="Portrait of the consultant in a teal jacket" style="left:86px;top:1395px;width:50px;height:110px;border-radius:25px 25px 0 0;background:linear-gradient(180deg,#d9cfc8 0%,#7d5b48 30%,#1f6f74 55%,#1a5f64 100%)"></div>
  <p class="abs" style="left:40px;top:1510px;width:150px;text-align:center;font-family:Tinos,serif;font-weight:700;font-size:5.5px;color:#111">Helena Marsh,&nbsp; CLS, NCMP, PhD</p>
  <div class="btn" style="left:83px;top:1525px;width:62px;height:11px;font-size:4.5px">CONSULTATION</div>

  <svg class="abs" style="left:0;top:1580px" width="230" height="30" viewBox="0 0 230 30" preserveAspectRatio="none"><path d="M0 18 C80 16 160 10 230 2" stroke="var(--orange)" stroke-width="3" fill="none"/><path d="M0 22 C80 20 160 14 230 6 L230 30 L0 30Z" fill="#000"/></svg>
  <footer class="footer" style="left:0;top:1608px;width:230px;height:372px">
    <svg class="abs" style="left:24px;top:32px" width="20" height="13" viewBox="0 0 34 22"><path d="M2 3h18v13H2zM20 8h7l5 5v3H20z" stroke="#fff" fill="none" stroke-width="2"/></svg>
    <p class="abs" style="left:56px;top:30px;font-size:5.5px;font-weight:700">Free shipping</p>
    <p class="abs accent" style="left:56px;top:40px;font-size:5.5px;font-weight:700">over $299</p>
    <svg class="abs" style="left:140px;top:31px" width="14" height="14" viewBox="0 0 28 28"><circle cx="14" cy="14" r="11" stroke="#fff" fill="none" stroke-width="2"/></svg>
    <p class="abs" style="left:164px;top:30px;font-size:5.5px;font-weight:700">Returns</p>
    <p class="abs accent" style="left:164px;top:40px;font-size:5.5px;font-weight:700">180-Day</p>
    <svg class="abs" style="left:108px;top:62px" width="14" height="12" viewBox="0 0 26 22"><path d="M2 4h22v14H2z M2 4l11 8 11-8" stroke="#fff" fill="none" stroke-width="2"/></svg>
    <p class="abs" style="left:0;width:230px;text-align:center;top:80px;font-size:5.5px;font-weight:700">Contact</p>
    <p class="abs" style="left:0;width:230px;text-align:center;top:96px;font-size:4.8px;line-height:10px">555 014-2268 Fairview, CA USA<br>info@TopWaveGoods.com<br>Modern Wellness Advisors LLC</p>
    <div class="abs" style="left:0;top:154px;width:230px;border-top:1px solid #333"></div>
    <div class="wordmark" style="left:0;width:230px;text-align:center;top:168px;font-size:16px;color:#fff">Bright Peb</div>
    <p class="abs col-title" style="left:21px;top:216px;font-size:5.5px">Quick Links</p>
    <p class="abs link" style="left:21px;top:230px;font-size:4.5px;line-height:12px">Search<br>Contact Information<br>Privacy Policy</p>
    <p class="abs col-title" style="left:95px;top:216px;font-size:5.5px">Other Links</p>
    <p class="abs link" style="left:95px;top:230px;font-size:4.5px;line-height:12px">Refund Policy<br>Shipping Policy<br>Terms of Service</p>
    <p class="abs col-title" style="left:164px;top:216px;font-size:5.5px">Follow Us</p>
    <span class="abs" style="left:170px;top:232px;width:5px;height:5px;border-radius:50%;background:#fff"></span>
    <span class="abs" style="left:182px;top:232px;width:5px;height:5px;background:#fff"></span>
    <p class="abs" style="left:0;width:230px;text-align:center;top:285px;font-size:5.5px;font-weight:700">Subscribe to our newsletter</p>
    <div class="abs" style="left:57px;top:302px;width:116px;height:18px;border-radius:10px;background:#fff;font-size:5px;color:#777;padding:5px 8px">Enter Email</div>
    <svg class="abs" style="left:155px;top:302px" width="18" height="18" viewBox="0 0 22 22"><circle cx="11" cy="11" r="11" fill="var(--orange)"/><path d="M7 6l9 5-9 5 2-5z" fill="#111"/></svg>
    <p class="abs" style="left:0;width:230px;text-align:center;top:330px;font-size:4px">Copyright@2024 - All Rights Reserved By Bright PEB</p>
    <div class="abs" style="left:40px;top:350px"><span class="pay" style="width:14px;height:8px;margin-right:4px"></span><span class="pay" style="width:14px;height:8px;margin-right:4px"></span><span class="pay" style="width:14px;height:8px;margin-right:4px"></span><span class="pay" style="width:14px;height:8px;margin-right:4px"></span><span class="pay" style="width:14px;height:8px;margin-right:4px"></span><span class="pay" style="width:14px;height:8px;margin-right:4px"></span><span class="pay" style="width:14px;height:8px;margin-right:4px"></span><span class="pay" style="width:14px;height:8px;margin-right:4px"></span></div>
  </footer>
</main>

</body>
</html>
```